Q-Rolls Business Card

We are a modern retail clothing store. Established in 1994. I need a presentable card that will amaze vendors when given to them.

Front: Logo in middle
Info Side:

Name: Tomas Velder
Cell: 630-812-4463
Work: 630-917-3384 EXT. 417
Email: Tomas@q-rolls-example.com
Website: www.Q-rolls-example.com

Industry/Entity Type

Business

```html
<!DOCTYPE html>
<html lang="en">
<head>
<meta charset="utf-8">
<title>Q-Rolls Business Card</title>
<link rel="stylesheet" href="https://fonts.googleapis.com/css2?family=Open+Sans:wght@400;700&display=swap">
<style>
  :root {
    --page-bg: #e4e1dc;
    --card-white: #ffffff;
    --card-shade: #ececec;
    --ink: #2e2e2e;
    --ink-soft: #6b6b6b;
    --band-black: #111111;
    --icon-bg: #3a3a3a;
  }
  * { margin: 0; padding: 0; box-sizing: border-box; }
  html, body {
    width: 1200px; height: 1023px; overflow: hidden;
    background: var(--page-bg);
  }
  .canvas { position: relative; width: 1200px; height: 1023px; }

  .card {
    position: absolute;
    width: 540px; height: 310px;
    left: 330px;
    border-radius: 8px 8px 44px 8px;
    box-shadow: 0 10px 28px rgba(0,0,0,0.18);
    overflow: hidden;
  }

  /* Front */
  .card-front {
    top: 120px;
    background: radial-gradient(ellipse at 45% 40%, var(--card-white) 40%, var(--card-shade) 100%);
    display: flex; align-items: center; justify-content: center;
  }
  .brand-name {
    font-family: "Open Sans", sans-serif;
    font-weight: 700;
    font-size: 58px;
    letter-spacing: 0;
    color: var(--ink);
  }

  /* Back */
  .card-back { top: 580px; background: var(--band-black); }
  .card-back .face { position: absolute; inset: 0; }
  .back-content { position: absolute; inset: 0; }
  .person { position: absolute; left: 34px; top: 30px; }
  .person-name {
    font-family: "Open Sans", sans-serif;
    font-weight: 700; font-size: 22px;
    letter-spacing: 0.5px; color: var(--ink);
    text-transform: uppercase;
  }
  .person-role {
    font-family: "Open Sans", sans-serif;
    font-size: 11px; color: var(--ink-soft); margin-top: 2px;
  }
  .contacts {
    position: absolute; left: 34px; bottom: 62px;
    list-style: none;
    font-family: "Open Sans", sans-serif;
    font-size: 13px; color: var(--ink);
  }
  .contacts li { display: flex; align-items: center; gap: 8px; height: 20px; }
  .contact-icon { width: 13px; height: 13px; flex: none; }
</style>
</head>
<body>
<main class="canvas">

  <section class="card card-front" aria-label="Card front">
    <span class="brand-name">Q-Rolls</span>
  </section>

  <section class="card card-back" aria-label="Card back">
    <svg class="face" width="540" height="310" viewBox="0 0 540 310" aria-hidden="true">
      <path d="M0 0 H500 V222 Q500 262 460 262 H0 Z" fill="var(--card-white)"/>
    </svg>
    <div class="back-content">
      <div class="person">
        <p class="person-name">Tomas Velder</p>
        <p class="person-role">Owner</p>
      </div>
      <ul class="contacts">
        <li>
          <svg class="contact-icon" viewBox="0 0 14 14" aria-hidden="true"><circle cx="7" cy="7" r="7" fill="var(--icon-bg)"/><rect x="4.5" y="3" width="5" height="8" rx="1" fill="#fff"/></svg>
          630-812-4463
        </li>
        <li>
          <svg class="contact-icon" viewBox="0 0 14 14" aria-hidden="true"><circle cx="7" cy="7" r="7" fill="var(--icon-bg)"/><path d="M4 4 Q3.5 7 7 10 Q9.5 11 10 10 L9 8.5 L8 9 Q6 8 5.5 6 L6 5 Z" fill="#fff"/></svg>
          630-917-3384 EXT. 417
        </li>
        <li>
          <svg class="contact-icon" viewBox="0 0 14 14" aria-hidden="true"><circle cx="7" cy="7" r="7" fill="var(--icon-bg)"/><rect x="3.5" y="4.5" width="7" height="5" fill="#fff"/><path d="M3.5 4.5 L7 7.5 L10.5 4.5" stroke="var(--icon-bg)" stroke-width="0.8" fill="none"/></svg>
          Tomas@q-rolls-example.com
        </li>
        <li>
          <svg class="contact-icon" viewBox="0 0 14 14" aria-hidden="true"><circle cx="7" cy="7" r="7" fill="var(--icon-bg)"/><circle cx="7" cy="7" r="3.6" fill="none" stroke="#fff" stroke-width="0.9"/><path d="M3.4 7 H10.6 M7 3.4 V10.6" stroke="#fff" stroke-width="0.8"/></svg>
          www.Q-rolls-example.com
        </li>
      </ul>
    </div>
  </section>

</main>
</body>
</html>
```